Zielgruppe
Seminare, Vorträge , Therapien, Beratung, Coaching
WEchseljahre Beratung
Sexualtherapie, Sexualberatung
Mentaltraining
Es soll Frauen gefallen und ermuntern zum Seminar zu kommen, frü Thema Wechseljahre interessieren
Aufgabenstellung
Grösse A5 Hochkant

```html
<!DOCTYPE html>
<html lang="de">
<head>
<meta charset="utf-8">
<title>Sonnenhof Frühjahrs Seminar Vol. 2 – Flyer</title>
<link rel="stylesheet" href="https://fonts.googleapis.com/css2?family=Open+Sans:wght@400;600;700&family=Cormorant+Garamond:wght@400;500&family=Dancing+Script:wght@600&display=swap">
<style>
:root{
  --bg:#e4e2df;
  --paper:#f7f6f6;
  --ink:#3a3a3c;
  --teal:#3fb8d2;
  --teal-soft:#8fd3e2;
  --lilac:#a58fc0;
  --lilac-soft:#b9acd3;
  --rose:#c9789f;
  --rose-text:#cc5a8f;
  --grey-band:#7d8c92;
}
*{box-sizing:border-box;margin:0;padding:0}
html,body{width:1200px;height:807px;overflow:hidden}
body{background:var(--bg);font-family:"Open Sans",Arial,sans-serif;color:var(--ink);position:relative}
.page{position:absolute;top:33px;width:523px;height:740px;background:var(--paper);overflow:hidden;box-shadow:0 2px 10px rgba(0,0,0,.18)}
.page--front{left:50px}
.page--back{left:627px}
.abs{position:absolute}
.photo{position:absolute}
.serif{font-family:"Cormorant Garamond",Georgia,serif;font-weight:500}

/* front */
.intro{left:28px;top:60px;font-size:15px;font-weight:600;line-height:1.25}
.title{left:26px;top:100px;font-size:38px;font-weight:700;line-height:1}
.subtitle{left:28px;top:146px;font-size:17px;font-weight:600}
.tagline{left:150px;top:174px;font-family:"Dancing Script",cursive;font-size:19px;color:var(--teal);line-height:1.05}
.photo--portrait-top{left:290px;top:0;width:233px;height:240px;background:radial-gradient(ellipse at 45% 45%,#d9c2b4 0%,#b7aaa4 40%,#e6e9ec 80%)}
.band{left:0;top:180px}
.brand-badge{left:385px;top:150px;width:96px;height:96px;border-radius:50%;background:var(--teal);border:3px solid #fff;display:flex;align-items:center;justify-content:center;text-align:center;color:#fff;font-size:10px;font-weight:600;line-height:1.2}
.band-text{left:305px;top:262px;width:200px;color:#fff;font-size:10px;line-height:1.3;transform:rotate(-8deg)}
.photo--circle{left:-20px;top:295px;width:180px;height:180px;border-radius:50%;border:4px solid var(--rose);background:radial-gradient(circle at 50% 35%,#d8b9a4 0%,#8b8fb9 55%,#9cb9a0 100%)}
.name-circle{left:145px;top:270px;width:124px;height:124px;border-radius:50%;background:var(--rose);border:4px solid #fff;color:#fff;text-align:center;padding-top:34px}
.name-circle .name{font-size:15px;font-weight:600}
.name-circle .roles{font-size:8px;line-height:1.3;margin-top:4px}
.front-heading{left:262px;top:336px;width:258px;font-size:19px;line-height:1.1;white-space:nowrap}
.front-body{left:262px;top:392px;width:250px;font-size:9.6px;line-height:1.45}
.photo--laughing{left:0;top:480px;width:255px;height:260px;background:radial-gradient(ellipse at 45% 40%,#d8ab94 0%,#7f6a64 40%,#2f3640 70%,#eaeaea 100%)}
.teal-box{left:260px;top:575px;width:263px;height:120px;background:var(--teal);color:#fff;font-size:10.5px;line-height:1.4;padding:18px 18px 0 26px}
.teal-box .url{position:absolute;right:14px;bottom:6px;font-size:10px}
.grey-strip{left:260px;top:695px;width:263px;height:45px;background:var(--grey-band)}

/* back */
.top-band{left:0;top:0}
.col-l{left:22px;width:235px}
.col-r{left:278px;width:230px}
.rule{height:1px;background:var(--rose);position:absolute}
.dot{width:10px;height:10px;border-radius:50%;background:var(--rose);position:absolute}
.h2{font-size:19px;line-height:1.05}
.list{list-style:none;font-size:9.3px;line-height:1.4}
.list li{padding-left:10px;position:relative}
.list li::before{content:"-";position:absolute;left:0}
.list--rose{color:var(--rose-text)}
.para{font-size:9.3px;line-height:1.45}
.para--rose{color:var(--rose-text)}
.photo--portrait-side{left:405px;top:335px;width:118px;height:200px;background:radial-gradient(ellipse at 45% 40%,#d9c2b4 0%,#b4a7a1 45%,#e6e9ec 85%)}
.corner{left:0;top:0}
.rose-circle{left:330px;top:495px;width:175px;height:175px;border-radius:50%;background:var(--rose);border:4px solid #fff;color:#fff;text-align:center;font-size:9.4px;line-height:1.35;padding:38px 20px 0}
.details{left:272px;top:338px;width:128px;text-align:center;font-size:9.5px;line-height:1.45;font-weight:600}
.contact{left:22px;top:598px;width:300px;font-size:9.5px;line-height:1.4;font-weight:600}
.contact .gap{height:6px}
</style>
</head>
<body>

<section class="page page--front" aria-label="Vorderseite">
  <div class="photo photo--portrait-top" role="img" aria-label="Foto einer lächelnden älteren Frau mit grauem Haar"></div>

  <svg class="abs band" width="523" height="160" viewBox="0 0 523 160" aria-hidden="true">
    <defs>
      <linearGradient id="bandGrad" x1="0" x2="1" y1="0" y2="0">
        <stop offset="0" stop-color="#3fb8d2"/>
        <stop offset=".55" stop-color="#a58fc0"/>
        <stop offset="1" stop-color="#b9acd3"/>
      </linearGradient>
    </defs>
    <path d="M0 120 C120 95 260 60 360 35 C430 18 480 10 523 5 L523 95 C420 100 300 115 0 150 Z" fill="url(#bandGrad)"/>
    <path d="M0 150 C200 125 380 100 523 92 L523 100 C380 110 200 135 0 160 Z" fill="#3fb8d2"/>
  </svg>

  <p class="abs intro">Seien auch Sie mit dabei am<br>23.04.2017</p>
  <h1 class="abs title">Sonnenhof</h1>
  <p class="abs subtitle">Frühjahrs Seminar - Vol. 2</p>
  <p class="abs tagline">Heiss Geschüttelt,<br>&nbsp;&nbsp;nicht kalt gerührt</p>

  <div class="abs brand-badge">Fachstelle<br>Talberg</div>
  <p class="abs band-text">Mit noch mehr Antworten und Tipps für diese spannende Zeit</p>

  <div class="photo photo--circle" role="img" aria-label="Foto einer sitzenden Frau in Jeans im Freien"></div>
  <div class="photo photo--laughing" role="img" aria-label="Foto einer lachenden Frau mit türkisem Schal, Daumen nach oben"></div>
  <div class="abs name-circle">
    <p class="name">Mira Talberg</p>
    <p class="roles">Sexualtherapeutin<br>Dipl. Wechseljahrberaterin<br>Mentaltrainerin</p>
  </div>

  <h2 class="abs front-heading serif">Über Abschied, Umbruch,<br>Sinnorientierung und Neuanfang.</h2>
  <p class="abs front-body">Die Wechseljahre sind keine Krankheit und sie kommen nicht über Nacht. Sie sind eine Einladung an uns Frauen, uns in den vielfältigen Veränderungen, die sich in Körper, Geist und Seele vollziehen, neu zu erfahren. Unsere wahre Schönheit und unser sinnliches Erleben sind von äußeren Dingen unabhängig und blühen gerade im Älterwerden auf eine neue und besondere Weise auf! Das Seminar zeigt auf, in welcher Form uns dabei die Hormone sogar unterstützen.</p>

  <div class="abs teal-box">
    Ein spannendes Tagesseminar über die Wechselbäder der Gefühle, über Hormone, Orientierung, Hilfen und Möglichkeiten. Über die Zeit davor, mittendrin und danach.
    <span class="url">www.herzlich-wachsen.ch</span>
  </div>
  <div class="abs grey-strip"></div>
</section>

<section class="page page--back" aria-label="Rückseite">
  <svg class="abs top-band" width="523" height="60" viewBox="0 0 523 60" aria-hidden="true">
    <defs>
      <linearGradient id="topGrad" x1="0" x2="1">
        <stop offset="0" stop-color="#8fd3e2"/>
        <stop offset="1" stop-color="#b9acd3"/>
      </linearGradient>
    </defs>
    <path d="M250 0 L523 0 L523 30 C460 40 380 30 250 10 Z" fill="url(#topGrad)"/>
    <path d="M0 0 L20 0 L20 740 L0 740 Z" fill="#8fd3e2" opacity=".35"/>
  </svg>

  <div class="photo photo--portrait-side" role="img" aria-label="Foto einer nachdenklich lächelnden älteren Frau"></div>
  <svg class="abs corner" width="523" height="740" viewBox="0 0 523 740" aria-hidden="true">
    <defs>
      <linearGradient id="cornerGrad" x1="0" x2="1" y1="0" y2="1">
        <stop offset="0" stop-color="#b9acd3"/>
        <stop offset="1" stop-color="#9aa6cf"/>
      </linearGradient>
    </defs>
    <path d="M330 620 C400 580 470 540 523 500 L523 740 L330 740 Z" fill="url(#cornerGrad)"/>
    <path d="M320 625 C400 580 470 540 523 495 L523 505 C470 550 400 590 330 630 Z" fill="#3fb8d2"/>
  </svg>

  <div class="dot" style="left:22px;top:38px"></div>
  <div class="rule" style="left:32px;top:43px;width:220px"></div>
  <h2 class="abs col-l h2 serif" style="top:52px">Kennen Sie diese Fragen?</h2>
  <ul class="abs col-l list" style="top:80px">
    <li>Wechseljahre, was heisst das für mich? Was passiert gerade mit mir?</li>
    <li>Was möchte ich vom Leben, welche Träume und Wünsche habe ich?</li>
    <li>Was kann ich für mich in dieser Zeit tun?</li>
    <li>Weshalb stelle ich so vieles in Frage und grübele?</li>
    <li>Weshalb kann ich so schlecht einschlafen oder durchschlafen?</li>
    <li>Soll ich Hormone nehmen, was gibt es sonst noch für Möglichkeiten?</li>
  </ul>

  <h2 class="abs col-l h2 serif" style="top:240px">Ein Neuwerden, ein Loslassen, ein einzigartiges Geschenk und Herausforderung zugleich!</h2>
  <p class="abs col-l para" style="top:312px">Viele Frauen befinden, dass mit dem Klimakterium eine Last von ihren Schultern fällt. Endlich dürfen sie sich fallen lassen, endlich an sich selbst denken. Für solche Frauen beginnt mit den hormonellen Wallungen eine Phase des Perspektivwechsels. Die Zeit des Klimakteriums lädt zu einer inneren Inventur und gegebenenfalls einer Neuorientierung ein.</p>
  <p class="abs col-l para para--rose" style="top:440px">Statt von einem Gefühlschaos überwältigt zu werden, empfinden sich viele Frauen als emotionell empfindsamer, zugänglicher und berührbarer. Moderatorin und Sängerin Lena Vorholt nimmt's mit Humor. Sie nennt die Wechseljahre ihren „inneren Sommer“ und träumt von einer implantierten Klimaanlage.</p>
  <div class="rule" style="left:32px;top:573px;width:220px"></div>
  <div class="dot" style="left:22px;top:568px"></div>

  <div class="abs contact">
    <p>Anmeldung unter:<br>www.zeitenwende-tag.ch / 079 / 41 26 830<br>info@herzlich-wachsen.ch</p>
    <div class="gap"></div>
    <p>Mira Talberg<br>Dipl. Wechseljahresberaterin,<br>Sexualtherapeutin und Mentaltrainerin<br>www.herzlich-wachsen.ch Ostrand</p>
  </div>

  <h2 class="abs col-r h2 serif" style="top:40px">Wenn Sie erfahren möchten,</h2>
  <ul class="abs col-r list" style="top:66px">
    <li>wie sich Ihr Körper in den Wechseljahren verändert,</li>
    <li>welche Beschwerden dadurch verursacht werden können</li>
    <li>was Sie aktiv zur Linderung und Vorbeugung beitragen können,</li>
    <li>wie Sie Ihre eigene Balance und Heilung finden</li>
  </ul>
  <h2 class="abs col-r h2 serif" style="top:190px">Wollen Sie wissen:</h2>
  <ul class="abs col-r list list--rose" style="top:216px">
    <li>Was mit Ihnen passiert und wie Sie diese neue Lebensphase auf natürliche Weise bewältigen und annehmen können</li>
    <li>Worum es wirklich geht in diesen Jahren</li>
    <li>Wie Sie mutig und lustvoll durch die Wechseljahre kommen</li>
    <li>Mehr wissen über Östrogene, Progesterone und Testosterone</li>
  </ul>

  <div class="abs details">
    <p>Datum: 23.04.2017</p>
    <br>
    <p>Seminar von 9.00 – 15.00 Uhr<br>Ort: Bildungshaus Lindenhof,<br>3912 Ravell<br>Kosten Seminar inkl. Getränke, Obst, Z'Nüni und 4 Gang</p>
  </div>

  <div class="abs rose-circle">Dieser Tag macht Mut zum Aufbruch und Neugier auf diese neue Lebensphase. Sie erleben, wie es sein wird, Altes loszulassen, den Blick nach vorn zu richten und wichtige Weichen für Ihren weiteren Lebensweg zu stellen.</div>
</section>

</body>
</html>
```